Etiketten für Basenpulver
Zielgruppe
Das Produkt ist ein Basenpulver, das Etikett sollte aber genauso gut für alle anderen Nahrungsergänzungsmittel einsetzbar sein.
Edles, seriöses Produkt, welches von Naturheilpraktikern und Ärzten empfohlen werden kann.
Soll trotzdem eine Assoziation von Lebendigkeit (Lebhaft) und Vita(-lisierend) drin haben.
Aufgabenstellung
Das Etikett ist für ein Basenpulver, das Grunddesign sollte jedoch auch für andere Nahrungsergänzungsmittel produkte funktionieren.
Die Verpackung ist eine 300g weiße Schraubverschluss Dose:
die Höhe des Etiketts: 67,7mm
die länge kann zwischen 97mm und 200mm variieren, je nach design.
Gerne auch zwei einzelne Etiketten mit jeweils den Maßen: 97mm * 67,7mm

```html
<!DOCTYPE html>
<html lang="de">
<head>
<meta charset="utf-8">
<title>Basenpulver Etikett</title>
<link href="https://fonts.googleapis.com/css2?family=Montserrat:wght@800;900&family=Oswald:wght@300;400;500&family=Raleway:wght@300&display=swap" rel="stylesheet">
<style>
  :root {
    --green: #5aac2e;
    --green-light: #bcdca4;
    --ink: #1e1e1e;
    --line: #555;
    --stage: #ececec;
    --paper: #ffffff;
  }
  * { box-sizing: border-box; margin: 0; padding: 0; }
  html, body { width: 1200px; height: 886px; overflow: hidden; background: var(--stage); }
  .label {
    position: absolute; left: 20px; top: 181px; width: 1160px; height: 523px;
    background: var(--paper); overflow: hidden;
    font-family: "Oswald", sans-serif; font-weight: 300; color: var(--ink);
  }
  .wave-band {
    position: absolute; left: 0; top: 0; width: 100%; height: 110px;
    background: linear-gradient(180deg, rgba(255,255,255,0) 0%, rgba(148,200,90,.55) 30%, rgba(110,180,60,.7) 55%, rgba(200,230,170,.4) 80%, rgba(255,255,255,0) 100%);
  }
  .block { position: absolute; white-space: nowrap; }
  .hl { color: var(--green); font-weight: 500; }

  /* left panel */
  .ingredients { left: 15px; top: 128px; font-size: 14px; line-height: 20px; letter-spacing: -0.2px; }
  .nutrition { position: absolute; left: 14px; top: 153px; width: 301px; height: 146px; border: 1px solid var(--line); padding-top: 6px; }
  .nutrition h2 { font-weight: 500; font-size: 17px; line-height: 24px; color: var(--green); padding: 0 7px 2px; }
  .row { display: grid; grid-template-columns: 64px 70px 58px 67px 40px; height: 24px; align-items: center; padding-left: 7px; font-size: 14px; }
  .row.shade { background: var(--green-light); }
  .usage { left: 15px; top: 308px; font-size: 14px; line-height: 19px; letter-spacing: -0.2px; }
  .note { left: 15px; top: 390px; font-size: 14px; line-height: 19px; letter-spacing: -0.2px; }
  .best-before { left: 15px; top: 475px; font-size: 14px; line-height: 19px; }

  /* centre panel */
  .front { position: absolute; left: 353px; top: 118px; width: 480px; text-align: center; }
  .title { font-family: "Montserrat", sans-serif; font-weight: 900; font-size: 98px; line-height: 86px; color: var(--green); letter-spacing: -3px; }
  .subtitle-word { font-family: "Montserrat", sans-serif; font-weight: 900; font-size: 38px; line-height: 40px; color: var(--green); letter-spacing: 34px; margin-right: -34px; margin-top: 6px; }
  .claim { font-family: "Raleway", sans-serif; font-weight: 300; font-size: 21px; line-height: 29px; margin-top: 8px; }
  .diet { font-family: "Montserrat", sans-serif; font-weight: 800; font-size: 19px; color: var(--green); margin-top: 12px; }
  .brand { display: flex; justify-content: center; align-items: center; gap: 12px; margin-top: 44px; }
  .brand-dot { width: 34px; height: 34px; border-radius: 50%; background: var(--green); }
  .brand-name { font-weight: 500; font-size: 54px; line-height: 60px; color: var(--green); letter-spacing: 2px; }

  /* right panel */
  .benefits { left: 848px; top: 120px; font-size: 17px; line-height: 23px; letter-spacing: -0.2px; }
  .badges { position: absolute; left: 849px; top: 202px; display: flex; gap: 14px; }
  .badge { width: 80px; text-align: center; font-size: 14px; line-height: 20px; }
  .badge-mark { width: 66px; height: 66px; border-radius: 50%; background: var(--green); margin: 0 auto 12px; }
  .maker { left: 848px; top: 357px; font-size: 17px; line-height: 23px; }
  .amount { left: 848px; top: 440px; font-size: 28px; line-height: 34px; font-weight: 400; }
</style>
</head>
<body>
<main class="label">
  <div class="wave-band" role="img" aria-label="Geschwungene grüne Lichtbänder als Kopfdekor"></div>

  <p class="block ingredients"><span class="hl">Inhalt:</span> Kaliumcitrat, Calciumcitrat, Magnesiumcitrat</p>
  <div class="nutrition">
    <h2>Nährwerttabelle:</h2>
    <div class="row shade"><span>Inhalt pro:</span><span>1ml=4,5g</span><span>%NRV</span><span>2ml=9g</span><span>%NRV</span></div>
    <div class="row"><span>Kalium</span><span>648mg</span><span>32,4</span><span>1296mg</span><span>64,8</span></div>
    <div class="row shade"><span>Calcium</span><span>378mg</span><span>42,25</span><span>756mg</span><span>84,5</span></div>
    <div class="row"><span>Magnesium</span><span>144mg</span><span>38,4</span><span>288mg</span><span>76,8</span></div>
  </div>
  <p class="block usage"><span class="hl">Verzehrsempfehlung:</span> 1-2 mal 1 gestrichenen Messlöffel<br>á 4,5g in 300ml natiumarmen Sprudel/Wasser auflösen.<br>Am besten zu Mahlzeiten trinken. Für die richtige Dosierung<br><span class="hl">vor jedem Öffnen schütteln!</span></p>
  <p class="block note"><span class="hl">Wichtiger Hinweis:</span> Nahrungsergänzungsmittel sind kein Ersatz<br>für eine ausgewogene und abwechslungsreiche Ernährung sowie eine<br>gesunde Lebensweise. Die empfohlene Verzehrmenge nicht überschrei-<br>ten. Außerhalb der Reichweite von kleinen Kindern aufbewahren.</p>
  <p class="block best-before hl">Mindestens haltbar bis: siehe Boden</p>

  <section class="front">
    <h1 class="title">BASEN</h1>
    <div class="subtitle-word">PULVER</div>
    <p class="claim">Mit basischen Mineralstoffen für die<br>Säure-Basen-Balance</p>
    <p class="diet">Vegan / Glutenfrei / Laktosefrei</p>
    <div class="brand"><span class="brand-dot"></span><span class="brand-name">LUMEN</span></div>
  </section>

  <p class="block benefits"><span class="hl">Basenpulver</span> trägt zu einer Verringerung von Müdig-<br>keit und einem normalen Säuren-Basen-Stoffwechsel<br>bei. Unterstützung gegen Übersäuerung.</p>
  <div class="badges">
    <div class="badge"><div class="badge-mark"></div>Keine künstlichen<br>Aromen oder<br>Süßungsmittel</div>
    <div class="badge"><div class="badge-mark"></div>Natriumarm<br>und<br>kaliumreich</div>
    <div class="badge"><div class="badge-mark"></div>Frei von<br>Zusatzstoffen</div>
  </div>
  <p class="block maker">Hergestellt in Deutschland<br>Lumen - Quelle der Natur - Kräuterweg 12<br>54321 Grünfeld - www.lumen-natur.de</p>
  <p class="block amount"><span class="hl">Inhalt 360g</span> = 60 Portionen</p>
</main>
</body>
</html>
```